Truck wrap Design For KV CLEANERS

Create unique and eye catching design with provide logo and information.
Also Add Cartoon or silhouette of a men with vacuum or steam cleaner.
Please Use attached template.
It must include logo that is attached. and information below:
--555-314-2097
--www.kvrapidwashpro.example
--kvrapid@wavenetmail.example
-- NFTCB MASKS TEXTILE CLEANER

Services:

Carpet, upholstery, Air duct, Dryer vent, Hard surface cleaning,

Residential/Commercial Services.

Target Market(s)

everyone

Colors

Designer to choose colors to be used in the design.

Requirements
Must have
• All the information that is provide in descricption
Should not have
• silly background.

```html
<!DOCTYPE html>
<html lang="en">
<head>
<meta charset="utf-8">
<title>KV Cleaners — Truck Wrap</title>
<link href="https://fonts.googleapis.com/css2?family=Bebas+Neue&family=Open+Sans:wght@400;700&display=swap" rel="stylesheet">
<style>
  :root {
    --page: #ffffff;
    --box-frame: #2358b0;
    --box-light: #2aa4ea;
    --box-mid: #1789d8;
    --band: #0f86d4;
    --strip: #1f5fb5;
    --cab: #1f5bab;
    --glass: #b9b9b9;
    --trim: #8e8e8e;
    --chassis: #232323;
    --tyre: #1e1e1e;
    --hub: #f2f2f2;
    --white: #ffffff;
  }
  html, body {
    margin: 0;
    width: 1200px;
    height: 1200px;
    overflow: hidden;
    background: var(--page);
  }
  .wrap-canvas { display: block; width: 1200px; height: 1200px; }
  .headline { font-family: "Bebas Neue", Impact, sans-serif; font-size: 38px; fill: var(--white); }
  .service-label { font-family: "Bebas Neue", Impact, sans-serif; font-size: 26px; fill: var(--white); }
  .tagline { font-family: "Open Sans", Arial, sans-serif; font-weight: 700; font-size: 14px; fill: var(--white); }
  .phone { font-family: "Bebas Neue", Impact, sans-serif; font-size: 40px; letter-spacing: 4px; fill: var(--white); }
  .contact { font-family: "Open Sans", Arial, sans-serif; font-size: 14px; fill: var(--white); }
  .brand-name { font-family: "Bebas Neue", Impact, sans-serif; font-size: 30px; fill: var(--box-frame); }
</style>
</head>
<body>
<svg class="wrap-canvas" viewBox="0 0 1500 1500" xmlns="http://www.w3.org/2000/svg">
  <defs>
    <linearGradient id="boxFill" x1="0" y1="0" x2="0" y2="1">
      <stop offset="0" stop-color="var(--box-light)"/>
      <stop offset="1" stop-color="var(--box-mid)"/>
    </linearGradient>
    <path id="headlineCurve" d="M360 552 Q560 505 820 484"/>
  </defs>

  <g class="cargo-box">
    <path d="M185 422 H935 Q980 422 980 470 V920 H185 Z" fill="var(--box-frame)"/>
    <rect x="200" y="452" width="735" height="423" fill="url(#boxFill)"/>
    <path class="title-band" d="M200 575 Q420 540 600 525 Q800 505 935 520 V600 Q780 565 600 570 Q400 580 200 610 Z" fill="var(--band)"/>
    <path class="lower-band" d="M200 760 Q450 730 640 720 Q820 705 935 690 V760 Q780 770 600 790 Q400 810 200 800 Z" fill="var(--band)" opacity="0.6"/>
    <rect class="base-strip" x="185" y="875" width="795" height="45" fill="var(--strip)"/>
    <rect x="216" y="438" width="24" height="6" rx="3" fill="var(--white)"/>
    <rect x="928" y="438" width="24" height="6" rx="3" fill="var(--white)"/>
    <rect x="216" y="884" width="24" height="6" rx="3" fill="var(--white)"/>
  </g>

  <text class="headline"><textPath href="#headlineCurve" textLength="405" lengthAdjust="spacing">NFTCB MASKS TEXTILE CLEANER</textPath></text>

  <g class="service-panels">
    <path role="img" aria-label="Photo of a patterned rug in a bright living room" d="M202 562 Q275 575 347 585 V742 Q275 735 202 722 Z" fill="#b7683f"/>
    <path role="img" aria-label="Photo of tufted brown leather upholstery" d="M349 585 Q420 585 494 575 V735 Q420 745 349 742 Z" fill="#4a241d"/>
    <path role="img" aria-label="Photo of copper air duct pipes against the sky" d="M496 575 Q570 560 641 545 V697 Q570 715 496 735 Z" fill="#6f9fc8"/>
    <path role="img" aria-label="Photo of an outdoor air conditioning and vent unit" d="M643 545 V530 H788 V685 Q715 690 643 697 Z" fill="#8a8f8e"/>
    <path role="img" aria-label="Photo of a rope-access worker cleaning a glass facade" d="M790 530 Q860 555 935 575 V710 Q860 690 790 685 Z" fill="#5f7f9e"/>
  </g>

  <g class="service-labels">
    <text class="service-label" transform="translate(228 738) rotate(14)">CARPET</text>
    <text class="service-label" transform="translate(376 768) rotate(-4)">UPHOLSTERY</text>
    <text class="service-label" transform="translate(552 745) rotate(-12)">AIR DUCT</text>
    <text class="service-label" transform="translate(682 715) rotate(-4)">DRYER VENT</text>
    <text class="service-label" transform="translate(812 712) rotate(8)">HARD SURFACE</text>
    <text class="service-label" transform="translate(824 738) rotate(8)">CLEANING</text>
  </g>

  <text class="tagline" transform="translate(342 818) rotate(-5)">Residential/Commercial Services.</text>
  <text class="phone" transform="translate(352 860) rotate(-4)">555-314-2097</text>
  <text class="contact" x="374" y="892">www.kvrapidwashpro.example</text>
  <text class="contact" x="374" y="910">kvrapid@wavenetmail.example</text>

  <g class="brand">
    <circle cx="752" cy="818" r="78" fill="var(--box-frame)"/>
    <circle cx="752" cy="818" r="70" fill="var(--white)"/>
    <text class="brand-name" x="752" y="829" text-anchor="middle">KV CLEANERS</text>
  </g>

  <g class="chassis">
    <rect x="147" y="920" width="840" height="20" fill="var(--chassis)"/>
    <path d="M210 940 H985 V1018 H668 V995 Q600 998 505 1000 Q470 950 430 950 Q380 950 350 1005 Q300 995 255 980 H210 Z" fill="var(--chassis)"/>
  </g>

  <g class="cab">
    <path d="M980 702 H1090 Q1125 705 1150 720 L1265 825 Q1360 845 1385 875 L1400 945 Q1412 990 1395 995 H1328 Q1310 920 1245 918 Q1180 920 1165 1005 H985 Z" fill="var(--cab)"/>
    <path d="M1005 740 Q1005 730 1018 730 H1085 Q1110 730 1130 750 L1200 832 H1005 Z" fill="var(--glass)"/>
    <path d="M1118 722 L1150 722 L1268 828 L1225 834 Z" fill="var(--glass)"/>
    <rect x="1132" y="788" width="32" height="44" rx="4" fill="#3a3a3a"/>
    <rect x="987" y="840" width="16" height="38" rx="2" fill="var(--trim)"/>
    <path d="M1350 878 Q1355 872 1390 875 L1398 935 H1350 Z" fill="#e4e4e4"/>
    <rect x="1355" y="900" width="40" height="18" fill="var(--trim)"/>
    <path d="M1310 942 H1412 V970 H1320 Z" fill="var(--trim)"/>
  </g>

  <g class="wheel rear">
    <circle cx="428" cy="1000" r="78" fill="var(--tyre)"/>
    <circle cx="428" cy="1000" r="46" fill="var(--hub)"/>
    <circle cx="428" cy="1000" r="16" fill="var(--tyre)"/>
  </g>
  <g class="wheel front">
    <circle cx="1245" cy="1005" r="72" fill="var(--tyre)"/>
    <circle cx="1245" cy="1005" r="46" fill="var(--hub)"/>
    <circle cx="1245" cy="1005" r="14" fill="#d0d0d0"/>
  </g>
</svg>
</body>
</html>
```